Thrifty Haul: Junk Removal - Website Design

We need a design and uploaded to Hostplume.com. I enclosed our postcard for reference too. I need a contact from at the top right so I can get leads.

Here are the sites I like:

https://carrybrisk.example/
https://www.1800tossbin.example
https://www.campusmoverscleardebris.example/junk-removal/
http://aroomfornanas.example/
http://www.driftwhirl.example/alternate/
https://www.servicemenautogifts.example/
http://www.wheelsforsoldiers.example/indexj/

```html
<!DOCTYPE html>
<html lang="en">
<head>
<meta charset="utf-8">
<title>Thrifty Haul – Junk Removal</title>
<link href="https://fonts.googleapis.com/css2?family=Oswald:wght@500;600;700&family=Roboto:ital,wght@0,400;0,500;0,700;1,400&display=swap" rel="stylesheet">
<style>
:root{
  --green:#7cb82f;
  --navy:#1d3d72;
  --navy-deep:#173463;
  --text:#7a7a7a;
  --dark:#333;
  --white:#fff;
}
*{box-sizing:border-box;margin:0;padding:0}
html,body{width:1200px;height:4090px;overflow:hidden;background:#fff}
body{position:relative;font-family:"Roboto",Arial,sans-serif;color:var(--text)}
.abs{position:absolute}
.display{font-family:"Oswald","Arial Narrow",sans-serif;font-weight:700;text-transform:uppercase;color:var(--navy);letter-spacing:.5px}
.btn{position:absolute;background:var(--green);color:#fff;font:700 14px "Roboto",sans-serif;text-transform:uppercase;display:flex;align-items:center;justify-content:center;gap:6px}
.btn .dot{width:12px;height:12px;border-radius:50%;background:#fff;display:inline-flex;align-items:center;justify-content:center}
.btn .dot::after{content:"";border-left:5px solid var(--green);border-top:3.5px solid transparent;border-bottom:3.5px solid transparent;margin-left:2px}
.center{left:0;width:1200px;text-align:center}
.rule{position:absolute;height:4px;display:flex}
.rule span:first-child{background:var(--navy);flex:3}
.rule span:last-child{background:var(--green);flex:1}
.photo{position:absolute}

/* top bar */
.topbar{left:452px;top:0;width:748px;height:59px;background:var(--green);clip-path:polygon(30px 0,100% 0,100% 100%,0 100%)}
.topbar .ring{position:absolute;width:40px;height:40px;border-radius:50%;background:var(--navy);border:3px solid #fff;top:9px}
.topbar .txt{position:absolute;color:#fff;font-weight:700}
.nav a{position:absolute;top:90px;font-size:14px;color:#444;text-decoration:none}
.nav a.active{color:var(--green)}
.logo{left:111px;top:68px;font:700 52px/1 "Oswald",sans-serif;color:var(--green);letter-spacing:1px}
.header-line{left:0;top:128px;width:1200px;height:3px;background:var(--green)}

/* quote */
.quote{left:801px;top:337px;width:399px;height:425px;background:var(--navy);border-top:5px solid var(--green)}
.quote h3{position:absolute;left:39px;top:32px;font:600 30px "Oswald",sans-serif;color:#fff}
.quote .field{position:absolute;left:39px;width:319px;height:38px;background:#fff;font-size:14px;color:#888;padding:10px 14px}
.quote .send{left:39px;top:339px;width:319px;height:40px;font-weight:500}

/* cards */
.card{position:absolute;width:310px;text-align:center}
.card .img{height:231px}
.card .icon{position:absolute;left:120px;top:196px;width:70px;height:70px;border-radius:50%;background:#fff;display:flex;align-items:center;justify-content:center}
.card h4{margin-top:36px;font:500 19px "Roboto",sans-serif;color:var(--navy);text-transform:uppercase}
.card p{margin-top:8px;font-size:13px;line-height:25.6px;padding:0 25px}
.card .btn{position:relative;margin:10px auto 0;width:146px;height:46px}

.para{font-size:14px;line-height:25.6px}

.why{position:absolute;width:230px;text-align:center}
.why .circle{width:90px;height:90px;margin:0 auto;border-radius:50%;background:var(--green);border:3px solid #fff;box-shadow:0 0 0 2px var(--green);display:flex;align-items:center;justify-content:center}
.why h5{margin-top:14px;font:700 18px "Roboto",sans-serif;color:var(--navy)}
.why p{margin-top:6px;font-size:13px;line-height:25px}

.footer{left:0;top:3703px;width:1200px;height:387px;background:var(--navy);border-top:6px solid var(--green)}
.footer h6{position:absolute;top:88px;font:500 26px "Oswald",sans-serif;color:#fff;text-transform:uppercase}
.footer .col{position:absolute;color:#fff;font-size:14px;line-height:26px}
.footer .mark{display:inline-block;width:8px;height:8px;background:#fff;border-radius:50%;margin-right:14px;vertical-align:middle}
</style>
</head>
<body>

<!-- Header -->
<div class="abs topbar">
  <div class="ring" style="left:58px">
    <svg width="34" height="34" viewBox="0 0 34 34"><path d="M12 10c1 0 2 3 2 4s-2 1-1 3 3 4 5 5 2-1 3-1 4 1 4 2-2 3-4 3c-5 0-12-7-12-12 0-2 2-4 3-4z" fill="#fff"/></svg>
  </div>
  <div class="txt" style="left:92px;top:18px;font-size:14px">Customer services : <span style="font-size:20px;font-weight:500">1-800-555-0142</span></div>
  <div class="ring" style="left:448px">
    <svg width="34" height="34" viewBox="0 0 34 34"><circle cx="17" cy="17" r="7" fill="none" stroke="#fff" stroke-width="2"/><path d="M17 13v4h3" stroke="#fff" stroke-width="2" fill="none"/></svg>
  </div>
  <div class="txt" style="left:500px;top:13px;font-size:21px">24/7 Services</div>
</div>

<div class="abs logo">THRIFTY HAUL</div>
<nav class="nav">
  <a class="active" style="left:428px">Home</a>
  <a style="left:495px">About us</a>
  <a style="left:584px">Junk Removal</a>
  <a style="left:706px">What we Do</a>
  <a style="left:817px">Blog</a>
  <a style="left:876px">Contact us</a>
  <a style="left:1003px;font-weight:700;color:#222">ENG ⌄</a>
</nav>
<div class="abs" role="img" aria-label="US flag language selector" style="left:1054px;top:80px;width:34px;height:34px;border-radius:50%;background:linear-gradient(#c8313b 0 15%,#fff 15% 30%,#c8313b 30% 45%,#fff 45% 60%,#c8313b 60% 75%,#fff 75% 90%,#c8313b 90%)"></div>
<div class="abs header-line"></div>

<!-- Hero -->
<div class="abs display center" style="top:188px;font-size:60px;color:var(--green)">Thrifty <span style="color:var(--navy)">Haul</span></div>
<p class="abs center para" style="top:262px;font-size:14px">Sed ut perspiciatis unde omnis iste natus error sit voluptatem accusantium doloremque laudantium, totam<br>rem aperiam, eaque ipsa quae ab illo inventore</p>
<div class="photo" role="img" aria-label="Smiling mover in red cap holding a branded box, with movers carrying a fridge, armchair and sofa" style="left:30px;top:325px;width:771px;height:375px;background:linear-gradient(90deg,#fff 0%,#eee8e6 30%,#d9c8c2 50%,#eee8e6 70%,#fff 100%)"></div>
<a class="btn" style="left:511px;top:327px;width:179px;height:48px;font-weight:500">Get Started <span class="dot"></span></a>
<svg class="abs" style="left:568px;top:634px" width="60" height="14">
  <circle cx="7" cy="7" r="5" fill="none" stroke="#aaa"/><circle cx="23" cy="7" r="5" fill="none" stroke="var(--green)" stroke-width="2"/><circle cx="38" cy="7" r="5" fill="none" stroke="#aaa"/><circle cx="53" cy="7" r="5" fill="none" stroke="#aaa"/>
</svg>

<section class="abs quote">
  <h3>GET A QUOTE</h3>
  <div class="field" style="top:79px">First Name</div>
  <div class="field" style="top:130px">Last Name</div>
  <div class="field" style="top:182px">Email</div>
  <div class="field" style="top:233px">Phone No</div>
  <div class="field" style="top:284px">Comments</div>
  <a class="btn send">SEND A REQUEST</a>
</section>

<!-- What we do -->
<h2 class="abs display center" style="top:780px;font-size:50px">What We Do</h2>
<div class="rule" style="left:560px;top:848px;width:80px"><span></span><span></span></div>

<div class="card" style="left:111px;top:878px">
  <div class="img" role="img" aria-label="Old washing machines in a garage" style="background:linear-gradient(135deg,#cfd3d6,#8d9398)"></div>
  <div class="icon"><svg width="40" height="40" viewBox="0 0 40 40" fill="none" stroke="#333" stroke-width="1.6"><path d="M6 20L20 8l14 12M10 17v15h20V17"/><rect x="16" y="24" width="8" height="8"/></svg></div>
  <h4>Residential</h4>
  <p>Sed ut perspiciatis unde omnis iste natus error sit voluptatem accusantium doloremque laudantium</p>
  <a class="btn">Learn More <span class="dot"></span></a>
</div>
<div class="card" style="left:446px;top:878px">
  <div class="img" role="img" aria-label="Two movers lifting a large box into a van" style="background:linear-gradient(135deg,#6b6660,#d8c6a8)"></div>
  <div class="icon"><svg width="40" height="40" viewBox="0 0 40 40" fill="none" stroke="#333" stroke-width="1.6"><rect x="6" y="14" width="18" height="14"/><path d="M24 18h6l4 5v5H24z"/><circle cx="12" cy="30" r="3"/><circle cx="29" cy="30" r="3"/></svg></div>
  <h4>Moving</h4>
  <p>Sed ut perspiciatis unde omnis iste natus error sit voluptatem accusantium doloremque laudantium</p>
  <a class="btn">Learn More <span class="dot"></span></a>
</div>
<div class="card" style="left:781px;top:878px">
  <div class="img" role="img" aria-label="Office workers carrying boxes in front of a brick wall" style="background:linear-gradient(135deg,#e9e5df,#b0543e)"></div>
  <div class="icon"><svg width="40" height="40" viewBox="0 0 40 40" fill="none" stroke="#333" stroke-width="1.6"><rect x="9" y="8" width="14" height="25"/><rect x="23" y="16" width="9" height="17"/><path d="M13 13h2M18 13h2M13 19h2M18 19h2M13 25h2M18 25h2"/></svg></div>
  <h4>Commercial</h4>
  <p>Sed ut perspiciatis unde omnis iste natus error sit voluptatem accusantium doloremque laudantium</p>
  <a class="btn">Learn More <span class="dot"></span></a>
</div>
<div class="card" style="left:111px;top:1332px">
  <div class="img" role="img" aria-label="Garage storage shelves with bins and a bicycle" style="background:linear-gradient(135deg,#d9d9d6,#6e6a66)"></div>
  <div class="icon"><svg width="40" height="40" viewBox="0 0 40 40" fill="none" stroke="#333" stroke-width="1.6"><path d="M7 14L20 7l13 7v19H7z"/><rect x="13" y="20" width="14" height="13"/><path d="M13 25h14M13 29h14"/></svg></div>
  <h4>Storage</h4>
  <p>Sed ut perspiciatis unde omnis iste natus error sit voluptatem accusantium doloremque laudantium</p>
  <a class="btn">Learn More <span class="dot"></span></a>
</div>
<div class="card" style="left:446px;top:1332px">
  <div class="img" role="img" aria-label="Rescue workers on a pile of storm debris" style="background:linear-gradient(135deg,#9a9590,#5b4a3c)"></div>
  <div class="icon"><svg width="40" height="40" viewBox="0 0 40 40" fill="none" stroke="#333" stroke-width="1.6"><path d="M7 18L18 9l11 9v14H7z"/><path d="M15 24l4 4 3-5 4 3M24 12l8-4"/></svg></div>
  <h4>Disasters</h4>
  <p>Sed ut perspiciatis unde omnis iste natus error sit voluptatem accusantium doloremque laudantium</p>
  <a class="btn">Learn More <span class="dot"></span></a>
</div>
<div class="card" style="left:781px;top:1332px">
  <div class="img" role="img" aria-label="House under renovation with scaffolding against blue sky" style="background:linear-gradient(160deg,#8fb3dc,#e9e6e0 60%,#c28a55)"></div>
  <div class="icon"><svg width="40" height="40" viewBox="0 0 40 40" fill="none" stroke="#333" stroke-width="1.6"><path d="M6 20L20 8l14 12M10 17v16h20V17"/><circle cx="20" cy="24" r="4"/></svg></div>
  <h4>Renovation</h4>
  <p>Sed ut perspiciatis unde omnis iste natus error sit voluptatem accusantium doloremque laudantium</p>
  <a class="btn">Learn More <span class="dot"></span></a>
</div>

<!-- Who we are -->
<div class="photo" role="img" aria-label="Two masked movers in blue uniforms holding branded boxes by a van" style="left:0;top:1857px;width:580px;height:460px;background:linear-gradient(135deg,#d7dbe0,#3f6fc0 55%,#c8a97a)"></div>
<div class="abs" style="left:584px;top:1876px;width:8px;height:441px;background:var(--green)"></div>
<div class="abs" style="left:592px;top:1876px;width:6px;height:441px;background:var(--navy)"></div>
<h2 class="abs display" style="left:643px;top:1870px;font-size:50px">Who We Are</h2>
<div class="rule" style="left:643px;top:1937px;width:100px"><span></span><span></span></div>
<p class="abs para" style="left:643px;top:1966px;width:440px">Sed ut perspiciatis unde omnis iste natus error sit voluptatem accusantium doloremque laudantium, totam rem aperiam, eaque ipsa quae ab illo inventore veritatis et quasi architecto beatae vitae dicta sunt explicabo. Nemo enim ipsam voluptatem quia voluptas sit aspernatur aut odit aut fugit, sed quia consequuntur magni dolores eos qui ratione voluptatem sequi nesciunt. Neque porro quisquam est, qui dolorem ipsum quia dolor sit amet, consectetur Sed ut perspiciatis unde omnis iste natus error sit voluptatem accusantium doloremque laudantium, totam rem aperiam, eaque ipsa quae ab illo inventore veritatis et quasi</p>
<a class="btn" style="left:643px;top:2243px;width:146px;height:47px">Learn More <span class="dot"></span></a>

<!-- Why choose us -->
<h2 class="abs display center" style="top:2398px;font-size:50px">Why Choose Us?</h2>
<div class="rule" style="left:560px;top:2463px;width:80px"><span></span><span></span></div>
<div class="why" style="left:118px;top:2518px">
  <div class="circle"><svg width="46" height="46" viewBox="0 0 46 46" fill="none" stroke="#fff" stroke-width="2"><path d="M10 36l18-18M14 10l22 22M30 10l6 6-4 4-6-6zM10 30l6 6"/></svg></div>
  <h5>On-Time Services</h5><p>Nemo enim ipsam voluptatem quia voluptas sit aspernatur aut</p>
</div>
<div class="why" style="left:363px;top:2518px">
  <div class="circle"><svg width="50" height="50" viewBox="0 0 50 50" fill="none" stroke="#fff" stroke-width="2"><circle cx="25" cy="25" r="17"/><text x="25" y="29" fill="#fff" stroke="none" font-size="11" font-family="Roboto" text-anchor="middle">24/7</text></svg></div>
  <h5>Full-services junk removal</h5><p>Nemo enim ipsam voluptatem quia voluptas sit aspernatur aut</p>
</div>
<div class="why" style="left:607px;top:2518px">
  <div class="circle"><svg width="46" height="46" viewBox="0 0 46 46" fill="none" stroke="#fff" stroke-width="2"><circle cx="24" cy="16" r="9"/><path d="M20 20l8-8M8 32h10l8 4 12-6M8 28v10"/></svg></div>
  <h5>Up front pricing</h5><p>Nemo enim ipsam voluptatem quia voluptas sit aspernatur aut</p>
</div>
<div class="why" style="left:852px;top:2518px">
  <div class="circle"><svg width="46" height="46" viewBox="0 0 46 46" fill="none" stroke="#fff" stroke-width="2"><rect x="10" y="10" width="14" height="10"/><rect x="24" y="20" width="12" height="16"/><path d="M10 26h10M10 31h10"/></svg></div>
  <h5>Covid-19 Compliant</h5><p>Nemo enim ipsam voluptatem quia voluptas sit aspernatur aut</p>
</div>

<!-- Testimonial -->
<section class="abs" role="img" aria-label="Blue tinted kitchen interior background" style="left:0;top:2785px;width:1200px;height:429px;background:linear-gradient(90deg,#24477f,#2c5190 50%,#24477f)"></section>
<h2 class="abs display center" style="top:2860px;font-size:50px;color:#fff">What Our Customer Says</h2>
<div class="rule" style="left:560px;top:2925px;width:80px"><span style="background:#fff"></span><span></span></div>
<p class="abs center" style="top:2964px;font-size:14px;font-style:italic;line-height:25.6px;color:#fff">“Nemo enim ipsam voluptatem quia voluptas sit aspernatur aut odit aut fugit, sed quia consequuntur magni dolores<br>eos qui ratione voluptatem sequi nesciunt. Neque porro quisquam est, qui dolorem ipsum quia dolor sit amet,<br>consectetur, adipisci velit, sed quia non numquam”</p>
<svg class="abs" style="left:106px;top:2978px" width="20" height="24"><path d="M14 3L5 12l9 9" stroke="#fff" stroke-width="2.5" fill="none"/></svg>
<svg class="abs" style="left:1074px;top:2978px" width="20" height="24"><path d="M6 3l9 9-9 9" stroke="#fff" stroke-width="2.5" fill="none"/></svg>
<div class="abs" role="img" aria-label="Customer portrait" style="left:492px;top:3051px;width:74px;height:74px;border-radius:50%;background:#b9cde3;border:3px solid #fff"></div>
<div class="abs" style="left:587px;top:3060px;font:500 20px 'Roboto',sans-serif;color:#fff">Sam Rivera</div>
<div class="abs" style="left:586px;top:3090px;font-size:15px;color:#f5c518;letter-spacing:2px">★★★★★</div>

<!-- Safety -->
<h2 class="abs display" style="left:111px;top:3298px;font-size:56px;line-height:52px">Your Safety Is Our<br>Top Priority</h2>
<div class="rule" style="left:111px;top:3418px;width:88px"><span></span><span></span></div>
<p class="abs para" style="left:111px;top:3440px;width:480px">Sed ut perspiciatis unde omnis iste natus error sit voluptatem accusantium doloremque laudantium, totam rem aperiam, eaque ipsa quae ab illo inventore veritatis et quasi architecto beatae vitae dicta sunt explicabo. Nemo enim ipsam voluptatem quia voluptas sit aspernatur aut odit aut fugit, sed quia consequuntur magni dolores eos qui ratione voluptatem sequi nesciunt. Neque porro quisquam est, qui dolorem ipsum quia dolor sit amet, consectetur</p>
<div class="photo" role="img" aria-label="Video still of a cleaner in yellow gloves working in a bright room" style="left:617px;top:3309px;width:472px;height:302px;background:linear-gradient(135deg,#eef0f2,#c9b48a 55%,#e1c24a)"></div>
<svg class="abs" style="left:814px;top:3421px" width="80" height="80"><circle cx="40" cy="40" r="40" fill="#7cb82f" opacity=".85"/><path d="M33 27l18 13-18 13z" fill="#fff"/></svg>

<!-- Footer -->
<footer class="abs footer">
  <h6 style="left:111px">About Thrifty Haul</h6>
  <p class="col" style="left:111px;top:128px;width:300px;font-size:13px;line-height:22px">Sed ut perspiciatis unde omnis iste natus error sit voluptatem accusantium doloremque laudantium, totam rem aperiam</p>
  <a class="btn" style="left:111px;top:212px;width:145px;height:45px">Learn More <span class="dot"></span></a>

  <h6 style="left:463px">Quick Links</h6>
  <div class="col" style="left:463px;top:128px">Home<br>About us<br>Junk Removal<br>What we Do<br>Blog<br>Contact us</div>

  <h6 style="left:678px">Contact Us</h6>
  <div class="col" style="left:678px;top:128px;width:240px">
    <svg width="10" height="14" style="position:absolute;left:0;top:6px"><path d="M5 0a5 5 0 015 5c0 4-5 9-5 9S0 9 0 5a5 5 0 015-5z" fill="#fff"/></svg>
    <div style="padding-left:26px">Sed ut perspiciatis unde omnis iste natus error sit vol</div>
    <svg width="12" height="12" style="position:absolute;left:0;top:84px"><path d="M3 0c1 0 2 2 2 3s-1 1-1 2 2 3 3 3 1-1 2-1 3 1 3 2-1 3-3 3C5 12 0 7 0 3c0-1 2-3 3-3z" fill="#fff"/></svg>
    <div style="padding-left:26px;margin-top:26px">+1-800-555-0142</div>
    <svg width="13" height="10" style="position:absolute;left:0;top:138px"><rect width="13" height="10" fill="#fff"/><path d="M0 0l6.5 5L13 0" stroke="#1d3d72" fill="none"/></svg>
    <div style="padding-left:26px;margin-top:26px">info@thriftyhaul.example</div>
  </div>

  <h6 style="left:952px">Follow Us</h6>
  <div class="col" style="left:952px;top:128px">
    <span class="mark"></span>Friendbook<br><span class="mark"></span>Chirper<br><span class="mark"></span>Snapgram<br><span class="mark"></span>Viewtube<br><span class="mark"></span>Worklinks
  </div>

  <div class="abs" style="left:0;top:302px;width:1200px;height:1px;background:rgba(255,255,255,.15)"></div>
  <div class="abs center" style="top:326px;font-size:14px;color:#fff">© Copyrights 2020 Company name | All Rights Reserved</div>
</footer>

</body>
</html>
```